Business Card for Wellness Clinic

We need a business card for our new logo. I want it to match the feel of the logo

Target Market(s)

Young professional families looking for holistic health care

Industry/Entity Type

Health And Wellness

Contact Information for Business Card

Our business Name: Brackenfield Health & wellness Centre, our phone #, email address...see attached old business card

Font styles to use
Sans Serif

Colors
33b8a4
cee9f5

Requirements
Must have
• my logo and business name
• Font is "Helvetica Neue LT Std 45 Light" and
• Only for "&" using font "Trajan pro bold"
• Use colors in the logo

```html
<!DOCTYPE html>
<html lang="en">
<head>
<meta charset="utf-8">
<title>Brackenfield Health &amp; Wellness Centre – Business Card</title>
<link rel="stylesheet" href="https://fonts.googleapis.com/css2?family=Lato:ital,wght@0,300;0,400;0,700;1,400&display=swap">
<style>
  :root {
    --teal: #2fb5a1;
    --charcoal: #333132;
    --white: #ffffff;
    --backdrop: #b4b3b3;
    --rule: #555555;
  }
  * { box-sizing: border-box; margin: 0; padding: 0; }
  html, body { width: 1200px; height: 900px; overflow: hidden; }
  body {
    background: var(--backdrop);
    font-family: "Lato", "Helvetica Neue", Arial, sans-serif;
    position: relative;
  }
  .card {
    position: absolute;
    width: 760px;
    height: 420px;
    background: var(--white);
    overflow: hidden;
    box-shadow: 0 10px 24px rgba(0,0,0,.25);
  }

  /* ---------- front ---------- */
  .card--front { left: 70px; top: 24px; }
  .edge-band {
    position: absolute; top: 0; bottom: 0; width: 30px;
    background: var(--charcoal);
  }
  .edge-band::after {
    content: ""; position: absolute; top: 0; bottom: 0; width: 6px;
    background: var(--teal);
  }
  .edge-band--left { left: 0; }
  .edge-band--left::after { right: 0; }
  .edge-band--right { right: 0; }
  .edge-band--right::after { left: 0; }

  .brand {
    position: absolute;
    text-align: center;
    color: var(--teal);
    font-weight: 300;
    letter-spacing: .18em;
    line-height: 1.25;
    text-transform: uppercase;
    white-space: nowrap;
  }
  .brand__mark {
    display: block; margin: 0 auto 14px;
    width: 38px; height: 38px; border-radius: 50%;
    background: var(--teal);
  }
  .card--front .brand { left: 50px; top: 128px; width: 330px; font-size: 20px; }

  .contact-panel {
    position: absolute; top: 0; right: 0; bottom: 0; width: 380px;
    background: var(--teal);
    clip-path: polygon(0 0, 100% 0, 100% 100%, 16% 100%);
  }
  .contact-panel__inner {
    position: absolute; inset: 0;
    background: var(--charcoal);
    clip-path: polygon(7px 0, 100% 0, 100% 100%, calc(16% + 7px) 100%);
    padding: 44px 0 0 58px;
  }
  .doctor__name { color: var(--white); font-weight: 700; font-size: 17px; }
  .doctor__name span { font-weight: 300; }
  .doctor__role { color: var(--teal); font-weight: 300; font-size: 17px; margin-bottom: 30px; }
  .contact-list { list-style: none; }
  .contact-list li {
    display: flex; align-items: flex-start; gap: 22px;
    color: var(--teal); font-size: 14.5px; line-height: 18px;
    margin-bottom: 10px; white-space: nowrap;
  }
  .contact-list li:nth-child(2) { padding-left: 6px; }
  .contact-list li:nth-child(3) { padding-left: 12px; }
  .contact-list li:nth-child(4) { padding-left: 18px; }
  .contact-list li:nth-child(5) { padding-left: 24px; line-height: 32px; }
  .contact-list svg { width: 15px; height: 15px; flex: none; fill: var(--white); margin-top: 2px; }
  .contact-list li:nth-child(5) svg { margin-top: 8px; }

  /* ---------- back ---------- */
  .card--back { left: 370px; top: 460px; }
  .card--back .brand { left: 230px; top: 30px; width: 300px; font-size: 19px; }
  .booking { position: absolute; left: 60px; right: 60px; color: var(--teal); font-size: 19px; }
  .booking__field {
    position: absolute; left: 0; right: 0;
    border-bottom: 1.5px solid var(--rule);
    padding-bottom: 2px;
  }
  .booking__field--date { top: 150px; right: 250px; }
  .booking__field--for { top: 188px; right: 250px; }
  .booking__field--time { top: 226px; left: 380px; }
  .booking__field--line { top: 266px; }
  .notice {
    position: absolute; left: 40px; right: 40px; top: 330px;
    color: var(--teal); font-size: 12.5px; font-style: italic; text-align: center;
    white-space: nowrap;
  }
</style>
</head>
<body>

  <section class="card card--front" aria-label="Business card front">
    <div class="edge-band edge-band--left"></div>
    <div class="brand">
      <span class="brand__mark"></span>
      Brackenfield Health<br>&amp; Wellness Centre
    </div>
    <div class="contact-panel">
      <div class="contact-panel__inner">
        <p class="doctor__name">Dr. Maren Holt, <span>B.Sc., N.D.</span></p>
        <p class="doctor__role">Naturopathic Doctor</p>
        <ul class="contact-list">
          <li><svg viewBox="0 0 24 24" aria-hidden="true"><path d="M6.6 10.8a15 15 0 0 0 6.6 6.6l2.2-2.2c.3-.3.7-.4 1-.2 1.1.4 2.3.6 3.6.6.6 0 1 .4 1 1V20c0 .6-.4 1-1 1A17 17 0 0 1 3 4c0-.6.4-1 1-1h3.5c.6 0 1 .4 1 1 0 1.3.2 2.5.6 3.6.1.3 0 .7-.2 1z"/></svg>613-555-0142</li>
          <li><svg viewBox="0 0 24 24" aria-hidden="true"><path d="M6 2h12v5H6zM3 8h18a1 1 0 0 1 1 1v8h-4v5H6v-5H2V9a1 1 0 0 1 1-1zm5 8v4h8v-4z"/></svg>888-555-0187</li>
          <li><svg viewBox="0 0 24 24" aria-hidden="true"><circle cx="12" cy="12" r="10"/><path d="M2 12h20M12 2c3 3 3 17 0 20M12 2c-3 3-3 17 0 20" stroke="#333132" stroke-width="1.6" fill="none"/></svg>www.brackenfieldnaturopathic.ca</li>
          <li><svg viewBox="0 0 24 24" aria-hidden="true"><path d="M2 5h20v14H2z"/><path d="M2 5l10 8 10-8" stroke="#333132" stroke-width="1.8" fill="none"/></svg>mholt@brackenfieldnaturopathic.ca</li>
          <li><svg viewBox="0 0 24 24" aria-hidden="true"><path d="M12 2a7 7 0 0 0-7 7c0 5 7 13 7 13s7-8 7-13a7 7 0 0 0-7-7zm0 9.5A2.5 2.5 0 1 1 12 6.5a2.5 2.5 0 0 1 0 5z"/></svg><span>48 Alder Lane, Unit 7B<br>Kingsbrook, ON L9T 3M8</span></li>
        </ul>
      </div>
    </div>
  </section>

  <section class="card card--back" aria-label="Appointment card back">
    <div class="edge-band edge-band--left"></div>
    <div class="edge-band edge-band--right"></div>
    <div class="brand">
      <span class="brand__mark"></span>
      Brackenfield Health<br>&amp; Wellness Centre
    </div>
    <div class="booking">
      <div class="booking__field booking__field--date">Date:</div>
      <div class="booking__field booking__field--for">For:</div>
      <div class="booking__field booking__field--time">Time:</div>
      <div class="booking__field booking__field--line">&nbsp;</div>
    </div>
    <p class="notice">If you are unable to keep your appointment, please provide at least 2 business days notice or full visit fees will apply.</p>
  </section>

</body>
</html>
```